Building Company Business Card Design

I am looking to get a business card designed for my Building Company. Please find the logo attached.

Industry/Entity Type

Business

Contact Information for Business Card

Mobile 0472 913 046
Email admin@tarrowconstructworks.com.au
Website www.tarrowconstructworks.com.au

Colors
0255a3

```html
<!DOCTYPE html>
<html lang="en">
<head>
<meta charset="utf-8">
<title>Tarrow Construct Works – Business Card</title>
<link rel="stylesheet" href="https://fonts.googleapis.com/css2?family=Open+Sans:wght@400;600&family=Oswald:wght@500&display=swap">
<style>
  :root {
    --page: #e6e4e1;
    --card: #232323;
    --blue: #2d5fb5;
    --white: #ffffff;
    --silver: #9a9a9a;
  }
  * { margin: 0; padding: 0; box-sizing: border-box; }
  html, body { width: 1200px; height: 1000px; overflow: hidden; }
  body {
    background: var(--page);
    position: relative;
    font-family: "Open Sans", Arial, sans-serif;
  }
  .card {
    position: absolute;
    left: 267px;
    width: 665px;
    height: 395px;
    background: var(--card);
    border-radius: 28px;
  }
  .card--front { top: 75px; }
  .card--back { top: 535px; }

  .brand-name {
    position: absolute;
    left: 0; right: 0;
    top: 176px;
    text-align: center;
    font-family: "Open Sans", Arial, sans-serif;
    font-weight: 600;
    font-size: 30px;
    letter-spacing: 2px;
    color: var(--silver);
  }

  .identity {
    position: absolute;
    right: 401px;
    top: 162px;
    text-align: right;
  }
  .identity__name {
    font-family: "Oswald", "Arial Narrow", sans-serif;
    font-weight: 500;
    font-size: 24px;
    line-height: 30px;
    color: var(--white);
    letter-spacing: 0.2px;
  }
  .identity__title {
    font-size: 16px;
    line-height: 22px;
    color: var(--blue);
  }
  .divider {
    position: absolute;
    left: 281px;
    top: 166px;
    width: 2px;
    height: 64px;
    background: var(--blue);
  }
  .contacts {
    position: absolute;
    left: 297px;
    top: 160px;
    list-style: none;
  }
  .contacts li {
    display: flex;
    align-items: center;
    height: 24px;
    font-size: 16px;
    color: var(--white);
  }
  .contacts svg {
    width: 14px;
    height: 14px;
    margin-right: 8px;
    fill: var(--blue);
    flex: none;
  }
  .address {
    position: absolute;
    left: 0; right: 0;
    top: 346px;
    text-align: center;
    font-size: 16px;
    color: var(--white);
  }
  .address__company { color: var(--blue); }
</style>
</head>
<body>

<section class="card card--front">
  <div class="brand-name">TARROW CONSTRUCT WORKS</div>
</section>

<section class="card card--back">
  <div class="identity">
    <div class="identity__name">DECLAN HARTLEY</div>
    <div class="identity__title">Managing Director</div>
  </div>
  <div class="divider"></div>
  <ul class="contacts">
    <li>
      <svg viewBox="0 0 16 16" aria-hidden="true"><path d="M1 5c0-2 3-3 7-3s7 1 7 3v1h-4V5H5v1H1z"/><path d="M3 7h10l1 7H2z"/></svg>
      + 000 000 0000
    </li>
    <li>
      <svg viewBox="0 0 16 16" aria-hidden="true"><path d="M1 3h14v10H1z M2 4l6 5 6-5z" fill-rule="evenodd"/></svg>
      info@tarrowconstructworks.com.au
    </li>
    <li>
      <svg viewBox="0 0 16 16" aria-hidden="true"><path d="M8 1a7 7 0 1 0 0 14A7 7 0 0 0 8 1zm0 2a5 5 0 0 1 4.6 3H10L8 4 6 6H3.4A5 5 0 0 1 8 3zM3.1 8H6l1 3-2 1.5A5 5 0 0 1 3.1 8z"/></svg>
      www.tarrowconstructworks.com.au
    </li>
  </ul>
  <p class="address"><span class="address__company">Tarrow Construct Works</span> - 57 Maple Road, Springfield, NY 100182</p>
</section>

</body>
</html>
```